Career Counselor in need of a business card design

Hello Creatives! I'm in need of a business card design for a new company based in Georgia, USA called Pathways By Lumen.

Some things that may be helpful in creating your concept(s) include:

My Logo (Included in the Files section): There are three versions, two versions are in the second file. The all gold stacked (vertical) version is my primary logo and then there are two horizontal versions (one is all gold and the other is gold and grey).

My mission: to empower tweens through young adults to realize and actualize their CAREER ASPIRATIONS.
My vision: for tweens through young adults to LIVE LIFE ON PURPOSE and become CONTRIBUTING MEMBERS OF SOCIETY.

Biblical scriptures that support my ‘Why’: Psalms 127: 3-4(NIV) Children are a heritage from the Lord, offspring a reward from him. Like ARROWS in the hands of a warrior are children…. And Proverbs 29:18(JKV) Where there is no VISION, the people perish.

*Words in ALL CAPS are to emphasize what's important to me and may possibly provide you some inspiration (IDK - Have fun with it)!

Target Market(s)

My ideal customers are parents, guardians, and young adults.

Contact Information for Business Card

My name, degrees and credential: Delmira Fosket, M.A., Ed.D., LPC
Title: Youth and Future Pathway Guide and Advisor

Number: 555.317.8842
Address: 2618 Velbrook Avenue., Suite 407, Fernhollow, OR 97999
Email: info@pathwaysbylumen.co
Website: www.pathwaysbylumen.co

My population: TWEENS • TEENS • EMERGING ADULTS
Services offered: One-On-One Sessions • Small Groups • Workshops

Colors

Designer to choose colors to be used in the design.

Requirements
Nice to have
• Either my mission or vision but I will understand if it does not all fit.
• My mission: To empower tweens through young adults to realize and actualize their career aspirations.
• My vision: For tweens through young adults to live life on purpose and become contributing members of society.

```html
<!DOCTYPE html>
<html lang="en">
<head>
<meta charset="utf-8">
<title>Pathways By Lumen — Business Card</title>
<link href="https://fonts.googleapis.com/css2?family=Lora:wght@400;600&display=swap" rel="stylesheet">
<style>
  :root {
    --page: #1b1c1e;
    --card-edge: #202224;
    --gold: #d9b13a;
    --gold-light: #f3d56a;
    --gold-dark: #a9821e;
    --text-grey: #c9c9c6;
    --faint: rgba(255,255,255,0.035);
  }
  * { box-sizing: border-box; margin: 0; padding: 0; }
  html, body { width: 1200px; height: 800px; overflow: hidden; }
  body {
    background: var(--page);
    font-family: "Lora", Georgia, serif;
    position: relative;
  }
  .card {
    position: absolute;
    left: 300px;
    width: 600px;
    height: 343px;
    background: radial-gradient(ellipse at 40% 30%, #2c2e30, var(--card-edge));
    overflow: hidden;
    box-shadow: 0 10px 30px rgba(0,0,0,0.5);
  }
  .card--front { top: 40px; }
  .card--back  { top: 417px; }

  .gold-band {
    position: absolute;
    left: 0; right: 0;
    bottom: 10px;
    height: 12px;
    background: linear-gradient(90deg, var(--gold-dark), var(--gold-light) 35%, var(--gold) 65%, var(--gold-light));
  }

  .brand {
    position: absolute;
    display: flex;
    align-items: center;
    gap: 18px;
  }
  .brand__mark {
    border: 4px solid var(--gold);
    border-radius: 50%;
    flex-shrink: 0;
  }
  .brand__rule {
    width: 1px;
    background: var(--gold);
    align-self: stretch;
  }
  .brand__name {
    color: var(--gold);
    font-weight: 600;
    letter-spacing: 1px;
    text-transform: uppercase;
    white-space: nowrap;
  }

  /* Front */
  .card--front .brand { left: 70px; top: 92px; }
  .card--front .brand__mark { width: 86px; height: 86px; }
  .card--front .brand__name { font-size: 30px; }
  .audience {
    position: absolute;
    left: 70px; right: 60px;
    top: 205px;
    color: var(--text-grey);
    font-size: 13.5px;
    letter-spacing: 1.6px;
    text-align: center;
  }
  .audience__rule {
    position: absolute;
    left: 60px; right: 60px;
    top: 230px;
    height: 1px;
    background: var(--gold);
    opacity: 0.7;
  }
  .services {
    position: absolute;
    left: 60px; right: 60px;
    top: 240px;
    color: var(--text-grey);
    font-size: 14px;
    letter-spacing: 0.6px;
    text-align: center;
  }
  .dot { color: var(--gold); }

  /* Back */
  .faint-ring {
    position: absolute;
    right: 30px; top: -40px;
    width: 300px; height: 300px;
    border-radius: 50%;
    border: 26px solid var(--faint);
  }
  .card--back .brand { left: 40px; top: 46px; }
  .card--back .brand__mark { width: 70px; height: 70px; }
  .card--back .brand__name { font-size: 24px; }

  .person {
    position: absolute;
    left: 40px; top: 148px;
  }
  .person__name {
    color: var(--gold);
    font-weight: 600;
    font-size: 21px;
  }
  .person__title {
    color: var(--text-grey);
    font-size: 14px;
    margin-top: 2px;
  }
  .divider {
    position: absolute;
    left: 40px; right: 40px;
    top: 204px;
    height: 1px;
    background: var(--gold);
    opacity: 0.6;
  }
  .contacts {
    position: absolute;
    left: 40px; top: 222px;
    list-style: none;
    color: var(--text-grey);
    font-size: 13.5px;
  }
  .contacts li {
    display: flex;
    align-items: center;
    gap: 10px;
    margin-bottom: 7px;
  }
  .contacts svg { width: 18px; height: 18px; flex-shrink: 0; }
  .address {
    position: absolute;
    right: 40px; top: 232px;
    text-align: right;
    color: var(--text-grey);
    font-size: 13.5px;
    font-style: normal;
    line-height: 1.55;
  }
</style>
</head>
<body>

<section class="card card--front" aria-label="Card front">
  <div class="brand">
    <span class="brand__mark" aria-hidden="true"></span>
    <span class="brand__rule" aria-hidden="true"></span>
    <span class="brand__name">Pathways By Lumen</span>
  </div>
  <p class="audience">TWEENS <span class="dot">•</span> TEENS <span class="dot">•</span> EMERGING ADULTS</p>
  <div class="audience__rule" aria-hidden="true"></div>
  <p class="services">One-On-One Sessions <span class="dot">•</span> Small Groups <span class="dot">•</span> Workshops</p>
  <div class="gold-band" aria-hidden="true"></div>
</section>

<section class="card card--back" aria-label="Card back">
  <div class="faint-ring" aria-hidden="true"></div>
  <div class="brand">
    <span class="brand__mark" aria-hidden="true"></span>
    <span class="brand__rule" aria-hidden="true"></span>
    <span class="brand__name">Pathways By Lumen</span>
  </div>

  <div class="person">
    <p class="person__name">Delmira Fosket, M.A., Ed.D., LPC</p>
    <p class="person__title">Youth and Future Pathway Guide and Advisor</p>
  </div>
  <div class="divider" aria-hidden="true"></div>

  <ul class="contacts">
    <li>
      <svg viewBox="0 0 20 20" aria-hidden="true"><circle cx="10" cy="10" r="9" fill="none" stroke="#d9b13a" stroke-width="1.4"/><rect x="7" y="5" width="6" height="10" rx="1" fill="none" stroke="#d9b13a" stroke-width="1.3"/></svg>
      555.317.8842
    </li>
    <li>
      <svg viewBox="0 0 20 20" aria-hidden="true"><circle cx="10" cy="10" r="9" fill="none" stroke="#d9b13a" stroke-width="1.4"/><rect x="5.5" y="7" width="9" height="6.5" fill="none" stroke="#d9b13a" stroke-width="1.2"/><path d="M5.5 7 L10 11 L14.5 7" fill="none" stroke="#d9b13a" stroke-width="1.2"/></svg>
      info@pathwaysbylumen.co
    </li>
    <li>
      <svg viewBox="0 0 20 20" aria-hidden="true"><circle cx="10" cy="10" r="9" fill="none" stroke="#d9b13a" stroke-width="1.4"/><circle cx="10" cy="10" r="5" fill="none" stroke="#d9b13a" stroke-width="1.1"/><ellipse cx="10" cy="10" rx="2.2" ry="5" fill="none" stroke="#d9b13a" stroke-width="1"/><line x1="5" y1="10" x2="15" y2="10" stroke="#d9b13a" stroke-width="1"/></svg>
      www.pathwaysbylumen.co
    </li>
  </ul>

  <address class="address">
    2618 Velbrook Avenue.<br>
    Suite 407, Fernhollow, OR 97999
  </address>

  <div class="gold-band" aria-hidden="true"></div>
</section>

</body>
</html>
```